Portfolio required for virtual assistant seeking new clients

I require an editable Word template that can be sent to clients. This is a new business venture I am undertaking - working as a virtual assistant (administration work). I will need to find my own clients so would like Wow factor. Target group will be small businesses/legal industry so needs to look professional.
The portfolio will need to note information about me, why hire me, my skill set and credentials. May add testimonials too. I have attached a draft of the amount of text required - still working on this.
I will upload my logo and business card design. I do like consistency.
Colours used Pantone 2745 C and 272 C. Open to other colours but would like to see the main colours of logo incorporated. Images welcome. May insert an image of myself at some stage so please allow for a spot for this photo.
The portfolio will need to be converted to pdf to send by email as well as printable.
Updates

Automatically set for 24 hours apologies did not see this. Now amended

```html
<!DOCTYPE html>
<html lang="en">
<head>
<meta charset="utf-8">
<title>Mara Kell – Virtual Assistant Portfolio</title>
<link rel="stylesheet" href="https://fonts.googleapis.com/css2?family=Jost:wght@400;500;600;700&family=Montserrat:wght@500;700&display=swap">
<style>
  :root{
    --stage:#8a8a8a;
    --paper:#ffffff;
    --navy:#2e3475;
    --lavender:#7b82c4;
    --ink:#1f1f24;
    --rule:#7b82c4;
  }
  *{box-sizing:border-box;margin:0;padding:0}
  html,body{width:1200px;height:720px;overflow:hidden;background:var(--stage)}
  body{position:relative;font-family:"Jost",sans-serif;color:var(--ink)}
  .page{position:absolute;top:122px;width:336px;height:475px;background:var(--paper);overflow:hidden}
  .page--about{left:60px}
  .page--services{left:433px}
  .page--credentials{left:804px}

  .footer{position:absolute;left:0;top:437px;width:100%;height:24px;background:var(--navy);
    color:#fff;font-size:6.6px;letter-spacing:.2px;display:flex;align-items:center;justify-content:space-between;padding:0 23px}

  .brand{position:absolute;left:0;width:100%;top:62px;display:flex;justify-content:center;align-items:center;gap:6px;
    color:var(--lavender);font-family:"Jost",sans-serif;font-weight:700;font-size:24px;letter-spacing:1px}
  .brand__dot{width:12px;height:12px;border-radius:50%;background:var(--lavender)}
  .title{position:absolute;left:0;width:100%;text-align:center;color:var(--navy);font-family:"Montserrat",sans-serif}
  .title--name{top:109px;font-size:23px;font-weight:700;letter-spacing:6px;padding-left:6px}
  .title--role{top:138px;font-size:12px;font-weight:500;letter-spacing:3.6px;padding-left:3.6px}

  .section-head{position:absolute;left:24px;right:24px;height:16px}
  .section-head__mark{position:absolute;left:0;top:1px;width:13px;height:13px;border:1.5px solid var(--lavender);border-radius:50%}
  .section-head__rule{position:absolute;left:26px;right:0;bottom:0;height:1px;background:var(--rule)}
  .section-head__text{position:absolute;left:41px;bottom:1px;font-weight:700;font-size:8.8px;color:var(--navy);letter-spacing:.1px}

  .copy{position:absolute;font-size:6.9px;line-height:8.1px}
  .copy p{margin-bottom:6.5px}
  .about-copy{left:65px;top:210px;width:248px;text-align:center}
  .about-copy p.left{text-align:left}
  .portrait{float:left;width:74px;height:74px;border-radius:50%;margin:3px 6px 0 -21px;shape-outside:circle(50%);
    background:radial-gradient(circle at 45% 40%,#d9c2ad 0,#a98c74 35%,#5b7390 70%,#2f4261 100%)}

  .why-copy{left:65px;top:72px;width:249px}
  .col{position:absolute;top:210px;font-size:6.9px;line-height:8.1px}
  .col--left{left:65px;width:128px}
  .col--right{left:196px;width:120px}
  .group{margin-bottom:8.1px}
  .group h3{font-size:6.9px;font-weight:700;color:var(--ink)}
  .group ul{list-style:none}
  .group li{position:relative;padding-left:8px}
  .group li::before{content:"";position:absolute;left:1px;top:3.5px;width:2px;height:2px;border-radius:50%;background:var(--ink)}

  .cred-list{left:65px;top:72px;width:250px;color:#333}
  .desk-photo{position:absolute;left:0;top:120px;width:336px;height:183px;
    background:linear-gradient(120deg,#a88a78 0%,#cdbfb3 30%,#e4dcd4 55%,#b9a4a0 80%,#9c8582 100%)}
</style>
</head>
<body>

<section class="page page--about">
  <div class="brand"><span class="brand__dot"></span>MKVA</div>
  <h1 class="title title--name">MARA KELL</h1>
  <div class="title title--role">VIRTUAL ASSISTANT</div>

  <div class="section-head" style="top:186px"><span class="section-head__mark"></span><span class="section-head__rule"></span><h2 class="section-head__text">ABOUT ME</h2></div>

  <div class="copy about-copy">
    <div class="portrait" role="img" aria-label="Portrait photo of the virtual assistant"></div>
    <p>Hello, I'm Mara Kell, a mother, coffee lover, and a passion for travel. I enjoy organisation and making life easy. With over 15 years of experience in the legal field, I have gained valuable experience whilst at the same time, perfecting my skills.</p>
    <p>Throughout my journey in the legal profession, I have held various roles, each contributing to my growth and expertise. Starting as a Rounds Clerk, I quickly advanced to the role of Administrative Assistant in the area of Litigation which involved leading a team of administration assistants focused on supporting legal professionals and litigation processes. This role was invaluable in that it taught me the importance of organisation, time management, attention to detail and multitasking.</p>
    <p class="left">I then transitioned into Debt Recovery, where I thrived as a Paralegal. In this role, I took on the responsibility of managing my own caseload and providing comprehensive legal support independently. Attention to detail, meticulous research and effective communication became second nature. This allowed me to achieve successful resolutions while maintaining the utmost organization and professionalism.</p>
  </div>

  <footer class="footer"><span>mara@mkva.com.au</span><span>|</span><span>0400 555 012</span><span>|</span><span>ABN: 12 345 678 901</span></footer>
</section>

<section class="page page--services">
  <div class="section-head" style="top:48px"><span class="section-head__mark"></span><span class="section-head__rule"></span><h2 class="section-head__text">WHY HIRE ME?</h2></div>
  <div class="copy why-copy">
    <p>A virtual assistant is an affordable alternative to hiring on-site administration support. Hire me for a once-off task or on a regular basis. I'm here to help you so get more time back in your day so you can focus on more important tasks. I want to save you time, as who has enough of that these days!</p>
    <p>I am known for my reliability, determination, ability to work diligently in fast-paced environments as well as delivering results. I take pride in my meticulous approach to the tasks I undertake. I adapt well to new technology.</p>
    <p>I am excited to embrace new opportunities that allow me to showcase my skill set expertise, provide dedicated support to professionals and that may involve my legal expertise. I am committed to making a positive impact wherever I go, bringing efficiency and structure.</p>
  </div>

  <div class="section-head" style="top:186px"><span class="section-head__mark"></span><span class="section-head__rule"></span><h2 class="section-head__text">WHAT CAN I DO FOR YOU?</h2></div>

  <div class="col col--left">
    <div class="group"><h3>General administration support</h3><ul>
      <li>Document preparation including editing and formatting</li><li>Spreadsheets</li><li>Client correspondence</li><li>Customer service / telephone calls</li><li>Invoicing</li><li>Bulk mail outs</li><li>Data entry</li><li>Database and records management</li></ul></div>
    <div class="group"><h3>Email management</h3><ul>
      <li>Categorize and prepare sub folders</li><li>Prioritize emails</li><li>Send email correspondence</li></ul></div>
    <div class="group"><h3>Calendar &amp; diary management</h3><ul>
      <li>Assist with scheduling appointments and meetings</li><li>Scheduling reminders</li></ul></div>
    <div class="group"><h3>Travel arrangements</h3><ul>
      <li>Assist with booking intrastate/interstate travel</li><li>Assist with car hire and accommodation</li></ul></div>
  </div>
  <div class="col col--right">
    <div class="group"><h3>Software</h3><ul><li>Quillsuite 365</li><li>Lexora Affinity</li><li>LEDGR</li></ul></div>
    <div class="group"><h3>Debt Collection</h3><ul>
      <li>Assist with sending out overdue statements</li><li>Issue demand letters</li><li>Issue Claims and enforcement action in the Magistrates Court of Eastvale</li><li>Negotiating payment arrangements</li><li>Knowledge with Courtvane portal</li></ul></div>
    <div class="group"><h3>Other</h3><ul><li>Online research</li><li>Event coordination</li></ul></div>
    <div class="group"><h3>Legal</h3><ul><li>Courtvane portal</li><li>Preparing Court documents</li><li>Filing Court Documents</li></ul></div>
  </div>

  <footer class="footer"><span>mara@mkva.com.au</span><span>|</span><span>0400 555 012</span><span>|</span><span>ABN: 12 345 678 901</span></footer>
</section>

<section class="page page--credentials">
  <div class="section-head" style="top:48px"><span class="section-head__mark"></span><span class="section-head__rule"></span><h2 class="section-head__text">CREDENTIALS</h2></div>
  <div class="copy cred-list">
    <div>Certificate IV in Business (Legal Services)</div>
    <div>Certificate III of Business Administration</div>
    <div>Certificate II in Business</div>
  </div>
  <div class="desk-photo" role="img" aria-label="Photo of hands typing on a laptop at a wooden desk with notebook, phone and small cactus"></div>
  <footer class="footer"><span>mara@mkva.com.au</span><span>|</span><span>0400 555 012</span><span>|</span><span>ABN: 12 345 678 901</span></footer>
</section>

</body>
</html>
```